i would like a business card to leave with customers and potential customers for electrical work and for the supply and install of reverse cycle airconditioning in the domestic and commercial market.
I own my own business and im a sole trader. I have an a'class electrical lisence and also a refrigeration lisence so i am
able to offer complete installations in airconditioning by a fully qualified and lisenced tradesman.
im looking for something that comes across as unique and professional.
i had the coluor black and some gold in mind but open to any coluors.
something like Beacon Electrical & Refrigeration
or Beacon Air.
i will use this design on a business card to advertise through summer to help generate installs through the busy season.

Target Market(s)

Mainly domestic house holds through summer who are in need of airconditioning and reliable information to acomadate thier cooling and heating requirements

Industry/Entity Type

Electrical

Requirements
Must have
• Business name- Beacon
My name- Peter Wollaston
My mobile no- 0457 819 302
My email- prwollaston@tarvel.com.au
Installation & Decomissioning of aiconditioning split systems
LIC NO: KTR 407516
Nice to have
• Beacon Electrical & Refrigeration

```html
<!DOCTYPE html>
<html lang="en">
<head>
<meta charset="utf-8">
<title>Beacon Electrical &amp; Refrigeration – Business Card</title>
<link rel="stylesheet" href="https://fonts.googleapis.com/css2?family=Arimo:wght@700&family=Ubuntu:wght@500&display=swap">
<style>
  :root {
    --card-white: #ffffff;
    --panel-gold: #f2c62f;
    --brand-ink: #27363a;
    --text-light: #ffffff;
    --text-edge: #3a2f08;
  }
  * { margin: 0; padding: 0; box-sizing: border-box; }
  html, body {
    width: 1200px;
    height: 642px;
    overflow: hidden;
    background: var(--card-white);
  }
  .card {
    position: relative;
    width: 1200px;
    height: 642px;
    display: flex;
  }
  .card-front {
    width: 763px;
    height: 100%;
    background: var(--card-white);
    display: flex;
    align-items: center;
    justify-content: center;
  }
  .brand {
    display: flex;
    align-items: center;
    gap: 26px;
    font-family: "Ubuntu", "Trebuchet MS", sans-serif;
    font-weight: 500;
    color: var(--brand-ink);
    margin-top: -20px;
  }
  .brand-mark {
    width: 74px;
    height: 74px;
    background: var(--panel-gold);
    flex: none;
  }
  .brand-name { display: flex; flex-direction: column; line-height: 1; }
  .brand-name .primary { font-size: 96px; letter-spacing: 1px; }
  .brand-name .secondary { font-size: 40px; margin-top: 12px; line-height: 1.1; }

  .card-back {
    width: 437px;
    height: 100%;
    background: var(--panel-gold);
    display: flex;
    flex-direction: column;
    align-items: center;
    font-family: "Arimo", Arial, sans-serif;
    font-weight: 700;
    color: var(--text-light);
    text-align: center;
    text-shadow:
      2px 0 0 var(--text-edge), -2px 0 0 var(--text-edge),
      0 2px 0 var(--text-edge), 0 -2px 0 var(--text-edge),
      2px 2px 3px rgba(0,0,0,.6);
  }
  .mini-brand {
    margin-top: 34px;
    display: flex;
    align-items: center;
    gap: 12px;
    font-family: "Ubuntu", "Trebuchet MS", sans-serif;
    font-weight: 500;
    color: var(--brand-ink);
    text-shadow: none;
    text-align: left;
    line-height: 1.05;
  }
  .mini-brand .brand-mark { width: 34px; height: 34px; background: var(--card-white); }
  .mini-brand .primary { font-size: 42px; display: block; }
  .mini-brand .secondary { font-size: 19px; display: block; }

  .owner-name { margin-top: 24px; font-size: 35px; letter-spacing: 1px; }
  .phone { margin-top: 24px; font-size: 42px; letter-spacing: 2px; }
  .email { margin-top: 20px; font-size: 20px; }
  .services { margin-top: 22px; font-size: 33px; line-height: 50px; }
  .licence { margin-top: auto; margin-bottom: 14px; font-size: 18px; letter-spacing: 1px; }
</style>
</head>
<body>
  <main class="card">
    <section class="card-front">
      <div class="brand">
        <span class="brand-mark" aria-hidden="true"></span>
        <div class="brand-name">
          <span class="primary">Beacon</span>
          <span class="secondary">Electrical &amp;<br>Refrigeration</span>
        </div>
      </div>
    </section>
    <section class="card-back">
      <div class="mini-brand">
        <span class="brand-mark" aria-hidden="true"></span>
        <div>
          <span class="primary">Beacon</span>
          <span class="secondary">Electrical &amp; Refrigeration</span>
        </div>
      </div>
      <p class="owner-name">Peter Wollaston</p>
      <p class="phone">0457 819 302</p>
      <p class="email">prwollaston@tarvel.com.au</p>
      <p class="services">Installation &amp;<br>Decomissioning<br>of airconditioning<br>split systems</p>
      <p class="licence">LIC NO: KTR 407516</p>
    </section>
  </main>
</body>
</html>
```